Flyer Design

Mobile (Dustless) Shot Blasting.Graffiti Removal, Brick and Stone restoration, Paint Stripping from garden gates to Ships.No job too big or Small.No Chemicals - just Air, Water and recycled abrasive.Fully pressure controlled to prevent damage to underlying surfaces.

Target Market(s)

Domestic and commercial

Industry/Entity Type

Paint

Requirements
Nice to have
• Before and after paint removal to bare steel.
• Before and after cleaned brick/ stone work and graffiti removal

```html
<!DOCTYPE html>
<html lang="en">
<head>
<meta charset="utf-8">
<title>Ridgeway Blasting – Mobile Dustless Shot Blasting Flyer</title>
<link href="https://fonts.googleapis.com/css2?family=Open+Sans:wght@400;600;700;800&display=swap" rel="stylesheet">
<style>
  :root {
    --green: #1f8a43;
    --green-dark: #13612c;
    --green-light: #2fa457;
    --charcoal: #3a3a3a;
    --charcoal-dark: #2b2b2b;
    --paper: #f2f2f2;
    --ink: #1d1d1d;
    --white: #ffffff;
  }
  * { margin: 0; padding: 0; box-sizing: border-box; }
  html, body { width: 940px; height: 1200px; overflow: hidden; background: var(--paper); }
  body { font-family: "Open Sans", Arial, sans-serif; color: var(--ink); }

  .flyer { position: relative; width: 940px; height: 1200px; background: var(--paper); overflow: hidden; }

  /* Header */
  .header-panel {
    position: absolute; left: 0; top: 0; width: 560px; height: 386px;
    background: linear-gradient(160deg, #444 0%, var(--charcoal) 55%, var(--charcoal-dark) 100%);
    border-bottom-right-radius: 60px;
  }
  .header-panel::after {
    content: ""; position: absolute; left: 0; right: 30px; bottom: 0; height: 6px;
    background: linear-gradient(90deg, var(--green-light), rgba(47,164,87,0));
  }
  .hero-photo {
    position: absolute; left: 444px; top: 0; width: 496px; height: 363px;
    background: linear-gradient(135deg, #7a3b2c 0%, #9c4a36 35%, #c9a23a 65%, #e6d06a 100%);
  }
  .brand {
    position: absolute; left: 70px; top: 90px; display: flex; align-items: center; gap: 18px;
  }
  .brand-dot { width: 58px; height: 58px; border-radius: 50%; background: var(--green-light); }
  .brand-name { font-weight: 800; font-size: 30px; color: var(--white); letter-spacing: 1px; }

  .title-banner {
    position: absolute; left: 0; top: 240px; width: 540px; height: 107px;
    background: linear-gradient(180deg, var(--green-light), var(--green-dark));
    clip-path: polygon(0 0, 100% 0, 93% 100%, 0 100%);
    color: var(--white); text-align: center; padding-right: 40px;
  }
  .title-sub { font-weight: 700; font-size: 27px; margin-top: 10px; }
  .title-main { font-weight: 800; font-size: 46px; letter-spacing: 5px; line-height: 1.15; }

  /* Body */
  .trailer-photo {
    position: absolute; left: 665px; top: 365px; width: 228px; height: 100px;
    background: linear-gradient(180deg, #2c8a44 0%, #1d6b33 60%, #333 100%);
    border-radius: 8px;
  }
  .company-heading {
    position: absolute; left: 42px; top: 440px;
    font-weight: 800; font-size: 30px; color: var(--ink);
  }
  .company-heading span { color: var(--green); }
  .intro {
    position: absolute; left: 42px; top: 488px; width: 850px;
    font-size: 19.5px; line-height: 1.45; color: #2a2a2a;
  }
  .features {
    position: absolute; left: 42px; top: 612px; width: 860px;
    display: grid; grid-template-columns: 465px 1fr; row-gap: 16px; list-style: none;
  }
  .features li { display: flex; align-items: center; gap: 12px; font-weight: 700; font-size: 23px; }
  .features svg { width: 24px; height: 24px; flex: none; }

  .pressure-bar {
    position: absolute; left: 42px; top: 775px; width: 854px; height: 47px;
    background: var(--charcoal); border-radius: 10px;
    color: var(--white); font-weight: 600; font-size: 20px;
    display: flex; align-items: center; justify-content: center; letter-spacing: .2px;
  }

  .gallery { position: absolute; left: 0; top: 842px; width: 940px; height: 230px; }
  .gallery-item {
    position: absolute; top: 0; width: 220px; height: 220px; border-radius: 50%;
    border: 5px solid var(--green);
    box-shadow: 0 0 0 4px var(--white), 0 22px 18px -14px rgba(0,0,0,.35);
  }
  .gallery-steps { left: 95px; background: linear-gradient(160deg, #b04a30, #7d3322 60%, #5a2a20); }
  .gallery-brick { left: 353px; background: linear-gradient(90deg, #e8e8e8 0%, #d9d6d0 48%, #6a4a38 52%, #5a3c2e 100%); }
  .gallery-hull { left: 613px; background: linear-gradient(180deg, #c9d6df 0%, #a46b5a 45%, #8e8e86 75%, #8aa05a 100%); }

  /* Footer */
  .footer {
    position: absolute; left: 0; top: 1091px; width: 940px; height: 109px;
    background: linear-gradient(180deg, var(--green-light), var(--green-dark));
    color: var(--white); text-align: center;
  }
  .footer::before {
    content: ""; position: absolute; left: 0; right: 0; top: 0; height: 4px; background: #5cc47c;
  }
  .call-line {
    display: flex; align-items: center; justify-content: center; gap: 16px;
    margin-top: 18px; font-size: 26px; font-weight: 600;
  }
  .call-line .phone { font-weight: 800; font-size: 32px; letter-spacing: 1px; }
  .call-line svg { width: 34px; height: 34px; }
  .contact-line { margin-top: 6px; font-size: 17px; font-weight: 600; }
</style>
</head>
<body>
<div class="flyer">
  <div class="hero-photo" role="img" aria-label="Worker in protective suit blasting graffiti off a brick wall"></div>
  <div class="header-panel"></div>

  <div class="brand">
    <div class="brand-dot"></div>
    <div class="brand-name">RIDGEWAY BLASTING</div>
  </div>

  <div class="title-banner">
    <div class="title-sub">MOBILE (DUSTLESS) SHOT</div>
    <div class="title-main">BLASTING</div>
  </div>

  <div class="trailer-photo" role="img" aria-label="Green mobile blasting unit on a twin-axle trailer"></div>

  <h1 class="company-heading">RIDGEWAY <span>BLASTING</span></h1>
  <p class="intro">Wet abrasive blasting is excellent for concrete or masonry restoration, thermoplastic road stripe removal, lead and asbestos paint abatement, sealer removal, parking lot grease spot removal, and many other applications. With wet abrasive blasting, the possibilities are endless.</p>

  <ul class="features">
    <li><svg viewBox="0 0 24 24"><rect x="2" y="2" width="18" height="18" rx="3" fill="none" stroke="#1f8a43" stroke-width="2.2"/><path d="M6 11l4 4 11-11" fill="none" stroke="#1f8a43" stroke-width="3" stroke-linecap="round"/></svg>Graffiti Removal</li>
    <li><svg viewBox="0 0 24 24"><rect x="2" y="2" width="18" height="18" rx="3" fill="none" stroke="#1f8a43" stroke-width="2.2"/><path d="M6 11l4 4 11-11" fill="none" stroke="#1f8a43" stroke-width="3" stroke-linecap="round"/></svg>No job too big or Small</li>
    <li><svg viewBox="0 0 24 24"><rect x="2" y="2" width="18" height="18" rx="3" fill="none" stroke="#1f8a43" stroke-width="2.2"/><path d="M6 11l4 4 11-11" fill="none" stroke="#1f8a43" stroke-width="3" stroke-linecap="round"/></svg>Brick and Stone restoration</li>
    <li><svg viewBox="0 0 24 24"><rect x="2" y="2" width="18" height="18" rx="3" fill="none" stroke="#1f8a43" stroke-width="2.2"/><path d="M6 11l4 4 11-11" fill="none" stroke="#1f8a43" stroke-width="3" stroke-linecap="round"/></svg>No Chemicals - just Air</li>
    <li><svg viewBox="0 0 24 24"><rect x="2" y="2" width="18" height="18" rx="3" fill="none" stroke="#1f8a43" stroke-width="2.2"/><path d="M6 11l4 4 11-11" fill="none" stroke="#1f8a43" stroke-width="3" stroke-linecap="round"/></svg>Paint Stripping</li>
    <li><svg viewBox="0 0 24 24"><rect x="2" y="2" width="18" height="18" rx="3" fill="none" stroke="#1f8a43" stroke-width="2.2"/><path d="M6 11l4 4 11-11" fill="none" stroke="#1f8a43" stroke-width="3" stroke-linecap="round"/></svg>Water and recycled abrasive</li>
  </ul>

  <div class="pressure-bar">FULLY PRESSURE CONTROLLED TO PREVENT DAMAGE TO UNDERLYING SURFACES</div>

  <div class="gallery">
    <div class="gallery-item gallery-steps" role="img" aria-label="Restored red brick steps, before and after cleaning"></div>
    <div class="gallery-item gallery-brick" role="img" aria-label="House front showing painted wall beside restored brickwork"></div>
    <div class="gallery-item gallery-hull" role="img" aria-label="Boat hull stripped back to bare steel"></div>
  </div>

  <div class="footer">
    <div class="call-line">
      <span>Call Daniel Hartley today at</span>
      <svg viewBox="0 0 34 34"><circle cx="17" cy="17" r="15" fill="none" stroke="#fff" stroke-width="2.5"/><path d="M11.5 9.5c1-.8 2-.6 2.6.4l1.6 2.6c.5.9.3 1.7-.5 2.3l-1 .8c.9 2 2.4 3.6 4.4 4.6l.8-1c.6-.8 1.5-1 2.3-.5l2.6 1.6c1 .6 1.2 1.6.4 2.6l-1 1.2c-.9 1-2.3 1.3-3.6.8-4.6-1.8-8.2-5.4-10-10-.5-1.3-.2-2.7.8-3.6z" fill="#fff"/></svg>
      <span class="phone">0770 900 4127</span>
    </div>
    <div class="contact-line">hello@ridgewayblasting.co.uk &nbsp;|&nbsp; www.ridgewayblasting.co.uk</div>
  </div>
</div>
</body>
</html>
```